Website Online Research Solutions

We are a small European high-tech online research company.
With our own state of the art software we run online panels and are conducting reseach for companies. Partly research via our own panel and partly via panels we maintain for our customers.
Our current website is old and outdatet: www.pravelo.nl.
We are in the process to change the content of the site. We want a modern, european and businesslike design for our new website.
Our logo has to stay the same (left uppersite of our website and attached) but can be changed a little to adapt it to the new design of the website. The colors of the site are up to you.
Target Market(s)
Marketeers and researchers of large and middle size companies in all kind of fields.
Industry/Entity Type
Online
Look and feel
Each slider illustrates characteristics of the customer's brand and the style your logo design should communicate.

```html
<!DOCTYPE html>
<html lang="nl">
<head>
<meta charset="utf-8">
<title>Pravelo - Online Research Solutions</title>
<link rel="stylesheet" href="https://fonts.googleapis.com/css2?family=Cabin:wght@400;500&family=Arimo&display=swap">
<style>
  :root {
    --page-bg: #1c1c1c;
    --panel-dark: #111111;
    --footer-bg: #3a3a3a;
    --tab-bg: #2c2c30;
    --tab-text: #8ab8ec;
    --accent-orange: #f08a24;
    --link-blue: #7fb1e6;
    --text-light: #ffffff;
    --text-muted: #c9c9c9;
    --text-dark: #1f1f1f;
    --rule: #4a4a4a;
    --hero-top: #ffffff;
    --hero-bottom: #cddcef;
  }
  * { box-sizing: border-box; margin: 0; padding: 0; }
  html, body { width: 967px; height: 1200px; overflow: hidden; }
  body {
    position: relative;
    background: var(--page-bg);
    font-family: "Cabin", sans-serif;
    color: var(--text-light);
  }
  a { text-decoration: none; }

  .brand { position: absolute; left: 44px; top: 14px; display: flex; align-items: center; }
  .brand-mark { width: 102px; height: 102px; border-radius: 50%; background: #f2f2f2; margin-right: 17px; }
  .brand-name { font-size: 27px; font-weight: 400; color: var(--text-light); }
  .brand-tagline { font-size: 21px; margin-left: 12px; color: var(--text-light); }

  .main-nav { position: absolute; left: 42px; top: 123px; width: 882px; height: 46px; display: flex; gap: 3px; }
  .main-nav a {
    flex: 1; display: flex; align-items: center; justify-content: center;
    background: var(--tab-bg); color: var(--tab-text);
    font-family: "Arimo", sans-serif; font-size: 17px;
    border-radius: 3px 3px 0 0;
  }
  .main-nav a.is-active { background: #fff; color: var(--accent-orange); }

  .hero {
    position: absolute; left: 42px; top: 169px; width: 882px; height: 255px;
    background: linear-gradient(to bottom, var(--hero-top) 45%, var(--hero-bottom));
    border-radius: 0 0 3px 3px; color: var(--text-dark);
  }
  .hero-title { position: absolute; left: 56px; top: 46px; font-size: 27px; font-weight: 400; line-height: 35px; }
  .hero-text { position: absolute; left: 56px; top: 134px; width: 440px; font-size: 16px; line-height: 21.5px; }
  .hero-visual {
    position: absolute; left: 545px; top: 26px; width: 325px; height: 205px;
    background: radial-gradient(ellipse at 55% 45%, #f4f4f4, #dfe3e8 70%, rgba(220,228,238,0));
    border-radius: 6px;
  }

  .specialities {
    position: absolute; left: 42px; top: 452px; width: 279px; height: 458px;
    background: var(--panel-dark); padding: 20px 24px 0 24px; border-radius: 2px;
  }
  .panel-title { font-size: 21px; font-weight: 400; padding-bottom: 10px; border-bottom: 1px solid var(--rule); margin-bottom: 10px; }
  .solution { margin-bottom: 19px; }
  .solution.is-last { margin-top: 24px; }
  .solution h3 { font-size: 18px; font-weight: 400; color: var(--link-blue); line-height: 22px; }
  .solution p { font-size: 14.5px; line-height: 20px; }
  .solution a { color: var(--accent-orange); }

  .button {
    display: inline-block; padding: 5px 19px;
    background: linear-gradient(to bottom, #f7a04a, #dd6a12);
    color: #1a1a1a; font-size: 14.5px; border-radius: 3px;
    border: 1px solid #b55a12;
  }
  .specialities .button { margin-top: 2px; }

  .newsletter {
    position: absolute; left: 42px; top: 925px; width: 279px; height: 110px;
    background: linear-gradient(to bottom, #ffffff, #cfdeef); color: var(--text-dark);
    padding: 12px 24px 0 24px; border-radius: 2px;
  }
  .newsletter h2 { font-size: 16.5px; font-weight: 400; padding-bottom: 8px; border-bottom: 1px solid #b9c2cc; }
  .newsletter-form { display: flex; align-items: center; margin: 11px 0 0 -6px; }
  .newsletter-form input {
    width: 184px; height: 23px; border: 1px solid #9aa3ad; padding: 0 9px;
    font-family: "Cabin", sans-serif; font-size: 13px; color: #666;
  }
  .newsletter-form .button { margin-left: 6px; padding: 2px 14px; font-size: 13px; }

  .content { position: absolute; left: 359px; top: 466px; width: 553px; height: 520px; }
  .content-title { font-size: 21px; font-weight: 400; padding-bottom: 12px; border-bottom: 1px solid var(--rule); }
  .content-lead { margin-top: 27px; width: 520px; font-size: 18px; line-height: 24px; color: var(--link-blue); }
  .content p.body { margin-top: 17px; width: 515px; font-size: 15px; line-height: 24px; }
  .content p.body + p.body { margin-top: 24px; }
  .site-list { list-style: none; margin-top: 24px; padding-left: 12px; font-size: 15px; line-height: 24px; }
  .site-list a { color: var(--accent-orange); }
  .content .button { position: absolute; right: 25px; top: 478px; }

  .site-footer {
    position: absolute; left: 42px; top: 1053px; width: 882px; height: 147px;
    background: var(--footer-bg); border-radius: 3px 3px 0 0; color: var(--text-muted);
  }
  .footer-col { position: absolute; top: 19px; }
  .footer-col h4 { font-size: 16.5px; font-weight: 400; margin-bottom: 14px; }
  .footer-col li { list-style: none; font-size: 13.5px; line-height: 18px; }
  .col-company { left: 30px; }
  .col-services { left: 230px; }
  .col-solutions { left: 437px; }
  .col-contact { left: 630px; }
  .col-contact h4 { margin-bottom: 12px; }
</style>
</head>
<body>
  <header class="brand">
    <span class="brand-mark"></span>
    <span class="brand-name">Pravelo</span>
    <span class="brand-tagline">- Online Research Solutions</span>
  </header>

  <nav class="main-nav">
    <a class="is-active" href="#">About us</a>
    <a href="#">Services</a>
    <a href="#">Solutions</a>
    <a href="#">Media</a>
    <a href="#">Staff</a>
    <a href="#">Contact us</a>
  </nav>

  <section class="hero">
    <h1 class="hero-title">Lorem ipsum dolor sit amet,<br>consectetur adipisicing.</h1>
    <p class="hero-text">Elit sed do eiusmod tempor incididunt ut labore et dolore magna aliqua. Ut enim ad minim veniam, quis nostrud exercitation ullamco laboris nisi ut aliquip ex.</p>
    <div class="hero-visual" role="img" aria-label="Illustration of a 3D pie chart resting on sheets of graph paper"></div>
  </section>

  <aside class="specialities">
    <h2 class="panel-title">We specialise in....</h2>
    <div class="solution"><h3>Solution one</h3><p>Lorem ipsum elit sed do eiusmod tempor incididunt... <a href="#">Read more</a></p></div>
    <div class="solution"><h3>Solution two</h3><p>Lorem ipsum elit sed do eiusmod tempor incididunt... <a href="#">Read more</a></p></div>
    <div class="solution"><h3>Solution three</h3><p>Lorem ipsum elit sed do eiusmod tempor incididunt... <a href="#">Read more</a></p></div>
    <div class="solution is-last"><h3>Solution four</h3><p>Lorem ipsum elit sed do eiusmod tempor incididunt... <a href="#">Read more</a></p></div>
    <a class="button" href="#">See more</a>
  </aside>

  <section class="newsletter">
    <h2>Subscribe to our Newsletter</h2>
    <form class="newsletter-form">
      <input type="text" value="your email address...">
      <a class="button" href="#">Join</a>
    </form>
  </section>

  <main class="content">
    <h2 class="content-title">Online Panels Solutions</h2>
    <p class="content-lead">Pravelo is gespecialiseerd in online gegevensverzameling en analyse en is werkzaam voor internationale opdrachtgevers.</p>
    <p class="body">Het bedrijf werd opgericht in 2003 en is gevestigd in Zeewaerde, een kleine havenplaats boven Amsterdam. Onze produkten zijn ontwikkeld op basis van Kwanta, een krachtige en uitermate flexibele onderzoekstool voor het verzamelen &amp; verwerken van (online) researchgegevens. Kwanta werd ontwikkeld dóór opinieonderzoekers vóór opinieonderzoekers.</p>
    <p class="body">Ons team bestaat uit zowel opinieonderzoekers als programmeurs met vele jaren ervaring op het gebied van opinieonderzoek en met name met online toepassingen daarvoor.</p>
    <p class="body">Deze bekende sites zijn ontwikkeld en worden beheerd door Pravelo BV:</p>
    <ul class="site-list">
      <li>&gt;&gt; <a href="#">www.stemvak.nl</a></li>
      <li>&gt;&gt; <a href="#">www.spiegelzaal.nl</a></li>
      <li>&gt;&gt; <a href="#">www.jongpanel.nl</a></li>
      <li>&gt;&gt; <a href="#">Korf klantenpanel</a></li>
    </ul>
    <a class="button" href="#">See more</a>
  </main>

  <footer class="site-footer">
    <div class="footer-col col-company"><h4>Company Info</h4><ul><li>About us</li><li>In the press</li><li>References</li><li>Contact us</li></ul></div>
    <div class="footer-col col-services"><h4>Services</h4><ul><li>Dataset publishing</li><li>Analysis</li><li>Service three</li><li>Service four</li></ul></div>
    <div class="footer-col col-solutions"><h4>Solutions</h4><ul><li>Solution one</li><li>Solution two</li><li>Solution three</li><li>Solution four</li></ul></div>
    <div class="footer-col col-contact"><h4>Pravelo BV</h4><ul><li>Havenkade 12, 1492 BK Zeewaerde</li><li>tel +31 (0)299 410220</li><li>fax +31 (0)299 410221</li><li>info@pravelo.nl</li></ul></div>
  </footer>
</body>
</html>
```